Need Flyer Design for real estate

Need a generic Flyer Design for real estate Company..

See few flyers attached for an ideas..need to have 4 directors pictures n contact details in one side (back side)..

Industry/Entity Type

Real Estate

Requirements
Must have
• Our Logo Colours..
• PANTONE 484 C ( RED)
• PANTONE 2766 C ( BLUE)

```html
<!DOCTYPE html>
<html lang="en">
<head>
<meta charset="utf-8">
<title>Meridian Real Estate Flyer</title>
<link href="https://fonts.googleapis.com/css2?family=Dosis:wght@300;400&family=Lato:wght@400;700&family=Pinyon+Script&display=swap" rel="stylesheet">
<style>
  :root {
    --navy: #1f2156;
    --red: #74121f;
    --white: #ffffff;
    --backdrop: #e6e6e8;
    --photo-light: #f1f0ec;
    --photo-mid: #d9d6cf;
  }
  * { margin: 0; padding: 0; box-sizing: border-box; }
  html, body { width: 1200px; height: 1039px; overflow: hidden; }
  body { background: var(--backdrop); position: relative; font-family: "Lato", sans-serif; }

  .flyer-front, .flyer-back {
    position: absolute; left: 140px; width: 921px; height: 395px;
    overflow: hidden; box-shadow: 0 2px 6px rgba(0,0,0,.25);
  }
  .flyer-front { top: 106px; background: var(--navy); }
  .flyer-back { top: 538px; background: var(--navy); height: 394px; }

  .front-art { position: absolute; inset: 0; }

  .brand {
    position: absolute; left: 528px; width: 344px; top: 100px; text-align: center;
    color: var(--white); font-family: "Dosis", sans-serif; font-weight: 400;
  }
  .brand-name { font-size: 40px; letter-spacing: 4px; line-height: 1; }
  .brand-name::before {
    content: ""; display: inline-block; width: 10px; height: 10px;
    background: var(--white); margin-right: 12px; vertical-align: middle;
  }
  .brand-sub { font-size: 8px; letter-spacing: 2px; margin-top: 2px; }

  .divider { position: absolute; left: 528px; width: 344px; height: 1px; background: rgba(255,255,255,.75); }
  .divider.top { top: 161px; }
  .divider.bottom { top: 308px; }

  .tagline {
    position: absolute; left: 528px; width: 344px; top: 170px; text-align: center;
    color: var(--white); font-family: "Dosis", sans-serif; font-weight: 300;
    font-size: 32px; line-height: 36px;
  }
  .tagline-script {
    display: block; font-family: "Pinyon Script", cursive; font-size: 66px;
    line-height: 62px; margin-top: -4px;
  }

  .web-band {
    position: absolute; left: 484px; right: 0; top: 322px; height: 49px;
    background: var(--red); border-radius: 25px 0 0 25px;
    color: var(--white); font-family: "Dosis", sans-serif; font-weight: 300;
    font-size: 28px; line-height: 49px; padding-left: 33px; letter-spacing: .2px;
  }

  .office-band {
    height: 56px; background: var(--red); color: var(--white);
    font-weight: 700; font-size: 26px; line-height: 58px; text-align: center;
  }
  .directors { display: flex; padding: 10px 0 0 53px; gap: 55px; height: 270px; }
  .director { width: 158px; color: var(--white); white-space: nowrap; }
  .director-photo { width: 158px; height: 171px; background: var(--white); }
  .director-name { font-size: 26px; margin-top: 6px; line-height: 27px; }
  .director-phone { font-size: 21.5px; line-height: 22px; margin-top: 2px; }
  .director-email { font-size: 18px; line-height: 20px; }

  .privacy {
    position: absolute; left: 0; right: 0; bottom: 0; height: 68px;
    background: var(--red); color: var(--white); padding: 8px 38px 0 37px;
  }
  .privacy-title { font-size: 12px; font-weight: 700; line-height: 14px; }
  .privacy-text { font-size: 6.8px; line-height: 9px; margin-top: 2px; }
</style>
</head>
<body>

<section class="flyer-front">
  <svg class="front-art" width="921" height="395" viewBox="0 0 921 395">
    <defs>
      <linearGradient id="photoTone" x1="0" y1="0" x2="1" y2="1">
        <stop offset="0" stop-color="var(--photo-light)"/>
        <stop offset="1" stop-color="var(--photo-mid)"/>
      </linearGradient>
    </defs>
    <path d="M0 0 H340 Q520 200 372 395 H0 Z" fill="url(#photoTone)" role="img" aria-label="Photo of a smiling couple in a bright new home"/>
    <path d="M344 0 Q528 200 380 395" fill="none" stroke="var(--red)" stroke-width="4"/>
  </svg>

  <div class="brand">
    <div class="brand-name">MERIDIAN</div>
    <div class="brand-sub">REAL ESTATE</div>
  </div>
  <div class="divider top"></div>
  <p class="tagline">WE CAN HELP YOU<br>TO FIND YOUR<span class="tagline-script">happy place</span></p>
  <div class="divider bottom"></div>
  <div class="web-band">WWW.MERIDIANREALESTATE.COM</div>
</section>

<section class="flyer-back">
  <h2 class="office-band">HARTWELL &amp; REED BAYFIELD/KINGSLEA/ NORTH HAVEN</h2>
  <div class="directors">
    <div class="director">
      <div class="director-photo" role="img" aria-label="Director portrait"></div>
      <p class="director-name">Your Name</p>
      <p class="director-phone">000 000 0000</p>
      <p class="director-email">emailhere@mail.com</p>
    </div>
    <div class="director">
      <div class="director-photo" role="img" aria-label="Director portrait"></div>
      <p class="director-name">Your Name</p>
      <p class="director-phone">000 000 0000</p>
      <p class="director-email">emailhere@mail.com</p>
    </div>
    <div class="director">
      <div class="director-photo" role="img" aria-label="Director portrait"></div>
      <p class="director-name">Your Name</p>
      <p class="director-phone">000 000 0000</p>
      <p class="director-email">emailhere@mail.com</p>
    </div>
    <div class="director">
      <div class="director-photo" role="img" aria-label="Director portrait"></div>
      <p class="director-name">Your Name</p>
      <p class="director-phone">000 000 0000</p>
      <p class="director-email">emailhere@mail.com</p>
    </div>
  </div>
  <div class="privacy">
    <p class="privacy-title">Privacy Acknowledgment:</p>
    <p class="privacy-text">We collect your personal information to help you buy, sell or lease property and to keep you informed about market updates, appraisals and new listings in your area. Your details are stored securely and are never sold to third parties. You may ask to view, correct or remove your information at any time by contacting our office directly. If you prefer not to receive further material from us, simply let us know and we will update our records promptly. By providing your details you agree to be contacted by our team about property services that may be of interest to you.</p>
  </div>
</section>

</body>
</html>
```